Business Card for a Life Coaching Company

BRAVOAK is a Life Coaching company that was initiated to support people who want to transform thier life or ana aspect of it.
our slogan is : "Dream. Believe. Succeed"
our logo is uploaded.
The name of the company implies that leadership, strength and wisdom required to change your life.
We want an attractive business card that would give an impression of reliability, support and change. so we really want it unique. Here are some examples of unique cards:

http://www.pixelcratehub.com/2009/05/100-really-creative-business-cards/

BravOak is a life coaching organization focusing on individual transformation through the application of relevant and timeless principles of success.  BravOak believes that real, sustainable life transformations are brought about by tuning into the timeless wisdom we each carry in our hearts while boldy acting in the direction of our dreams.

Contacts on the card:
Address: 7 Sharia Nour El Din Zamalek Cairo Egypt
Tel: +202 24 31 57 18
Fax: +202 24 31 57 02
Mobile: +2 012 748 2396 (Dalia Haddad)
+2 0199915815 (Tariq Mansoor)

By the way, our temporary website is http://www.bravoak.com

We have attached an .eps file with various configurations of our logo.

```html
<!DOCTYPE html>
<html lang="en">
<head>
<meta charset="utf-8">
<title>BRAVOAK Business Card</title>
<link rel="stylesheet" href="https://fonts.googleapis.com/css2?family=Crimson+Text&display=swap">
<style>
  :root {
    --backdrop: #e6e5e6;
    --card: #ffffff;
    --brand-orange: #ff6a00;
    --brand-grey: #8f8f8f;
  }
  html, body {
    margin: 0;
    padding: 0;
    width: 1050px;
    height: 1200px;
    overflow: hidden;
    background: var(--backdrop);
    font-family: "Crimson Text", Georgia, serif;
  }
  .canvas {
    position: relative;
    width: 1050px;
    height: 1200px;
  }
  .card {
    position: absolute;
    left: 190px;
    width: 680px;
    height: 388px;
    background: var(--card);
    overflow: hidden;
  }
  .card--front { top: 165px; }
  .card--back { top: 620px; }

  .brand {
    position: absolute;
    left: 36px;
    top: 152px;
    display: flex;
    align-items: center;
    gap: 12px;
  }
  .brand__square {
    width: 34px;
    height: 34px;
    background: var(--brand-orange);
  }
  .brand__name {
    font-size: 44px;
    line-height: 1;
    letter-spacing: 1px;
    color: var(--brand-grey);
  }

  .slogan {
    position: absolute;
    left: 286px;
    top: 161px;
    width: 394px;
    height: 50px;
    box-sizing: border-box;
    border: 2px solid var(--brand-orange);
    border-right: none;
    padding-left: 12px;
    display: flex;
    align-items: center;
    font-size: 22px;
    color: var(--brand-orange);
  }

  .contact {
    position: absolute;
    left: 0;
    top: 82px;
    width: 404px;
    text-align: center;
    color: var(--brand-orange);
    font-size: 17.5px;
    line-height: 30px;
  }
  .contact p { margin: 0; }
  .contact__group { margin-top: 24px; }
  .contact__group--tight { margin-top: 22px; line-height: 29px; }
  .contact__web { margin-top: 16px; }

  .card__pattern {
    position: absolute;
    left: 396px;
    top: 0;
    width: 284px;
    height: 388px;
    background: var(--brand-orange);
  }
</style>
</head>
<body>
<div class="canvas">
  <section class="card card--front">
    <div class="brand">
      <span class="brand__square"></span>
      <span class="brand__name">BRAVOAK</span>
    </div>
    <div class="slogan">"Dream. Believe. Succeed"</div>
  </section>

  <section class="card card--back">
    <div class="contact">
      <p>7 Sharia Nour El Din Zamalek Cairo Egypt</p>
      <div class="contact__group">
        <p>(Dalia Haddad)+2 012 748 2396</p>
        <p>(Tariq Mansoor)+2 0197342618</p>
      </div>
      <div class="contact__group contact__group--tight">
        <p>Tel: +202 24 31 57 18</p>
        <p>Fax: +202 24 31 57 02</p>
      </div>
      <p class="contact__web">www.bravoak.com</p>
    </div>
    <div class="card__pattern" role="img" aria-label="Bold orange brush-stroke mane pattern"></div>
  </section>
</div>
</body>
</html>
```